New business card design for Pinecrest Hollow Optometry Clinic

We need a new business card design using our existing logo (uploaded). Please do not include eyes, eye exam charts or beaches, water, sand. The logo I uploaded shows our colors of green and blue, but we are open to seeing it in black OR white. We would like to see something modern and fresh. It will need to be 2 sided. On the front we will need to be able to put a doctors name, for example-Dr Marta Kellerman and Associates. We will need to be able to change the name to other doctors names when we send for printing. The back of the card should list the following: 3817 Tarrow St, Wasaga Beach (P)705-555-0148 (E) info@phoc.ca www.phoc.ca. "We are welcoming new patients" and a line for the appointment date and time. I have uploaded the back of a card to give an example

```html
<!DOCTYPE html>
<html lang="en">
<head>
<meta charset="UTF-8">
<title>Pinecrest Hollow Optometry Clinic – Business Card</title>
<link href="https://fonts.googleapis.com/css2?family=Montserrat:wght@400;500;700&display=swap" rel="stylesheet">
<style>
  :root {
    --clinic-blue: #3a51a3;
    --clinic-green: #1f9a48;
    --card-white: #ffffff;
    --page-bg: #e6e9f1;
    --watermark: #f1f3f8;
  }
  * { margin: 0; padding: 0; box-sizing: border-box; }
  html, body {
    width: 1200px; height: 1200px; overflow: hidden;
    background: var(--page-bg);
    font-family: "Montserrat", Arial, sans-serif;
  }
  .canvas { position: relative; width: 1200px; height: 1200px; }
  .card {
    position: absolute; left: 164px; width: 871px; height: 513px;
    background: var(--card-white); overflow: hidden;
  }
  .card-front { top: 75px; }
  .card-back { top: 618px; }

  /* Front */
  .clinic-name {
    position: absolute; left: 0; right: 0; top: 120px;
    text-align: center; color: var(--clinic-blue);
    font-weight: 700; font-size: 52px; line-height: 1.12; letter-spacing: -0.5px;
  }
  .contact-band {
    position: absolute; left: 0; bottom: 0; width: 100%; height: 203px;
    background: var(--clinic-blue);
  }
  .band-swoosh { position: absolute; left: 0; top: 0; width: 871px; height: 203px; }
  .doctor-name {
    position: absolute; left: 54px; top: 57px;
    color: var(--card-white); font-weight: 500; font-size: 28px; line-height: 1.18;
  }
  .contact-list {
    position: absolute; right: 66px; top: 52px; list-style: none;
    color: var(--card-white); font-size: 20px; line-height: 33px; text-align: right;
  }
  .contact-list li { display: flex; justify-content: flex-end; align-items: center; gap: 10px; }
  .contact-icon { width: 14px; height: 14px; flex: none; }

  /* Back */
  .back-watermark {
    position: absolute; left: 0; right: 0; top: 150px;
    text-align: center; color: var(--watermark);
    font-weight: 700; font-size: 88px; line-height: 1.1;
  }
  .welcome-line {
    position: absolute; left: 0; right: 0; top: 128px;
    text-align: center; color: var(--clinic-green);
    font-weight: 500; font-size: 40px;
  }
  .appointment-field {
    position: absolute; color: var(--clinic-blue); font-size: 27px;
    display: flex; align-items: baseline;
  }
  .field-dots {
    flex: 1; border-bottom: 3px dotted var(--clinic-blue); margin-left: 4px; height: 1px;
  }
  .field-doctor { left: 124px; top: 240px; width: 622px; }
  .field-date { left: 124px; top: 318px; width: 374px; }
  .field-time { left: 498px; top: 318px; width: 248px; }
</style>
</head>
<body>
<main class="canvas">

  <section class="card card-front" aria-label="Card front">
    <h1 class="clinic-name">Pinecrest Hollow<br>Optometry Clinic</h1>
    <div class="contact-band">
      <svg class="band-swoosh" viewBox="0 0 871 203" aria-hidden="true">
        <path d="M336 203 C 380 110, 440 40, 534 0 L 548 0 C 470 48, 400 120, 346 203 Z" fill="#ffffff"/>
      </svg>
      <p class="doctor-name">Dr Marta Kellerman<br>and Associates</p>
      <ul class="contact-list">
        <li>705-555-0148
          <svg class="contact-icon" viewBox="0 0 16 16" aria-hidden="true"><path d="M4 1.5l2.3 3-1.4 1.6c.8 1.9 2.3 3.4 4.2 4.2l1.6-1.4 3 2.3-1.3 2.6C7 13.6 2.4 9 1.4 2.8z" fill="#fff"/></svg>
        </li>
        <li>info@phoc.ca www.phoc.ca
          <svg class="contact-icon" viewBox="0 0 16 16" aria-hidden="true"><rect x="1" y="3" width="14" height="10" fill="#fff"/><path d="M1.5 3.5L8 9l6.5-5.5" stroke="#3a51a3" stroke-width="1.4" fill="none"/></svg>
        </li>
        <li>3817 Tarrow St, Wasaga Beach
          <svg class="contact-icon" viewBox="0 0 16 16" aria-hidden="true"><path d="M8 1a4.5 4.5 0 0 1 4.5 4.5C12.5 9 8 15 8 15S3.5 9 3.5 5.5A4.5 4.5 0 0 1 8 1z" fill="#fff"/><circle cx="8" cy="5.5" r="1.7" fill="#3a51a3"/></svg>
        </li>
      </ul>
    </div>
  </section>

  <section class="card card-back" aria-label="Card back">
    <p class="back-watermark" aria-hidden="true">Pinecrest Hollow<br>Optometry Clinic</p>
    <h2 class="welcome-line">We are Welcoming New Patients!</h2>
    <div class="appointment-field field-doctor"><span>Doctor:</span><span class="field-dots"></span></div>
    <div class="appointment-field field-date"><span>Date:</span><span class="field-dots"></span></div>
    <div class="appointment-field field-time"><span>Time:</span><span class="field-dots"></span></div>
  </section>

</main>
</body>
</html>
```